I would like a single page website for Kestrel Lift Rentals. In the file list provided there is basic information to be included as well as our logo with colors, fonts and images to be included.
Site must be very simple and be able to be loaded onto smart phones etc very quickly.
Site needs to be very smart in appearance

Target Market(s)

All prospective drone customers from Police to Parties.

Industry/Entity Type

Hire

Coding

Coded - Design and coding required

Number of Pages Required

1 page

Requirements
Must have
• Must have variation of color schemes supplied
Nice to have
• Must be very eye catching without going over the top
Should not have
• Anything slow to load.

```html
<!DOCTYPE html>
<html lang="en">
<head>
<meta charset="utf-8">
<title>Kestrel Lift Rentals</title>
<link rel="stylesheet" href="https://fonts.googleapis.com/css2?family=Barlow+Semi+Condensed:wght@500;600&family=Open+Sans:wght@300;400;600;700&display=swap">
<style>
  :root {
    --navy: #35467a;
    --ink: #333333;
    --body: #555555;
    --green: #5aa63a;
    --grey-band: #e4e4e4;
    --white: #ffffff;
    --footer: #2c2c2c;
    --footer-text: #8a8a8a;
    --footer-icon: #555555;
  }
  * { margin: 0; padding: 0; box-sizing: border-box; }
  html, body { width: 1200px; height: 2853px; overflow: hidden; }
  body { position: relative; background: var(--white); font-family: "Open Sans", Arial, sans-serif; color: var(--body); }
  section, footer, header { position: absolute; left: 0; width: 1200px; }
  .abs { position: absolute; }

  /* Hero */
  .hero { top: 0; height: 603px; overflow: hidden; }
  .hero-photo { position: absolute; inset: 0;
    background: linear-gradient(160deg, #c9d3cf 0%, #b9b48a 25%, #8a8d5c 45%, #4f5a3b 70%, #3d4636 100%); }
  .hero-photo::after { content: ""; position: absolute; inset: 0;
    background: radial-gradient(circle at 88% 10%, rgba(255,240,170,.85) 0%, rgba(255,230,140,.3) 22%, rgba(0,0,0,0) 45%); }
  .brand { left: 99px; top: 46px; color: var(--navy); font-family: "Barlow Semi Condensed", Arial, sans-serif; font-weight: 600; line-height: 1; }
  .brand .name { font-size: 44px; letter-spacing: 1px; }
  .brand .sub { font-size: 22px; letter-spacing: 9px; margin-top: 4px; }
  .nav { top: 70px; left: 0; width: 1200px; }
  .nav a { position: absolute; font-size: 13px; font-weight: 700; color: #1f1f1f; text-decoration: none; letter-spacing: .3px; }
  .menu-btn { left: 1064px; top: 59px; width: 37px; height: 37px; border: 2px solid #222; display: flex; align-items: center; justify-content: center; }
  .hero-title { left: 99px; top: 444px; color: var(--white); font-size: 29px; line-height: 40px; text-shadow: 0 1px 3px rgba(0,0,0,.35); }
  .hero-title strong { font-weight: 700; display: block; }
  .hero-title span { font-weight: 300; display: block; }

  /* Shared headings */
  .section-title { width: 1200px; text-align: center; font-family: "Barlow Semi Condensed", Arial, sans-serif; font-weight: 600; font-size: 29px; color: var(--navy); letter-spacing: .5px; }
  .section-lead { width: 1200px; text-align: center; font-size: 12px; line-height: 26px; color: var(--body); }

  /* Welcome */
  .welcome { top: 603px; height: 571px; background: var(--white); }
  .feature { width: 300px; text-align: center; }
  .feature svg { display: block; margin: 0 auto; }
  .feature h3 { font-size: 15px; font-weight: 600; color: var(--ink); margin-top: 16px; }
  .feature p { font-size: 11.5px; line-height: 26px; margin-top: 12px; padding: 0 28px; }

  /* Videos */
  .videos { top: 1174px; height: 570px; background: var(--grey-band); }
  .monitor { left: 99px; top: 78px; width: 486px; height: 420px; }
  .monitor-bezel { position: absolute; left: 0; top: 0; width: 486px; height: 300px; background: #1c1c1c; border-radius: 14px 14px 0 0; }
  .monitor-screen { position: absolute; left: 19px; top: 19px; width: 448px; height: 262px;
    background: linear-gradient(180deg, #c7b98a 0%, #bfa866 35%, #8a7a4a 62%, #d9b64e 80%, #a98a3a 100%); }
  .monitor-chin { position: absolute; left: 0; top: 300px; width: 486px; height: 52px; background: linear-gradient(180deg, #f2f2f2, #d6d6d6); border-radius: 0 0 14px 14px; }
  .monitor-stand { position: absolute; left: 168px; top: 352px; width: 150px; height: 68px; background: linear-gradient(180deg, #c8c8c8, #9a9a9a); clip-path: polygon(18% 0, 82% 0, 100% 100%, 0 100%); }
  .video-copy { left: 668px; top: 104px; width: 345px; }
  .video-copy .eyebrow { font-family: "Barlow Semi Condensed", Arial, sans-serif; font-weight: 600; font-size: 27px; color: var(--navy); line-height: 32px; }
  .video-copy h2 { font-family: "Barlow Semi Condensed", Arial, sans-serif; font-weight: 600; font-size: 35px; color: var(--navy); line-height: 40px; letter-spacing: .5px; }
  .video-copy p { font-size: 11.5px; line-height: 24.5px; margin-top: 14px; }
  .btn { display: inline-block; margin-top: 24px; width: 183px; height: 47px; line-height: 47px; text-align: center; background: var(--green); color: var(--white); font-size: 13px; text-decoration: none; }

  /* Posts */
  .posts { top: 1744px; height: 556px; background: var(--white); }
  .post { width: 228px; }
  .post-img { width: 228px; height: 145px; }
  .post h4 { font-size: 12.5px; font-weight: 700; color: var(--ink); margin-top: 20px; }
  .post p { font-size: 11.5px; line-height: 24px; margin-top: 6px; }

  /* Clients */
  .clients { top: 2300px; height: 374px; background: var(--grey-band); }
  .client { top: 201px; width: 192px; height: 103px; background: var(--white); display: flex; align-items: center; justify-content: center; gap: 8px; color: #8d8d8d; font-size: 22px; font-weight: 600; }
  .client i { width: 14px; height: 14px; border-radius: 50%; background: #bdbdbd; display: block; }

  /* Footer */
  .site-footer { top: 2674px; height: 179px; background: var(--footer); }
  .footer-links { top: 45px; width: 1200px; text-align: center; font-size: 11px; color: var(--footer-text); }
  .footer-links span.sep { margin: 0 20px; }
  .copyright { top: 76px; width: 1200px; text-align: center; font-size: 11px; color: var(--footer-text); }
  .social { top: 112px; left: 514px; display: flex; gap: 10px; }
  .social i { display: block; width: 28px; height: 28px; border-radius: 50%; background: var(--footer-icon); }
</style>
</head>
<body>

<header class="hero">
  <div class="hero-photo" role="img" aria-label="Aerial photograph of a riverside city with a white camera drone hovering at right"></div>
  <div class="abs brand"><div class="name">KESTREL LIFT</div><div class="sub">RENTALS</div></div>
  <nav class="abs nav">
    <a style="left:506px">HOME</a>
    <a style="left:606px">ABOUT US</a>
    <a style="left:728px">SERVICES</a>
    <a style="left:845px">VIDEOS</a>
    <a style="left:951px">CONTACT US</a>
  </nav>
  <div class="abs menu-btn">
    <svg width="16" height="13" viewBox="0 0 16 13"><rect width="16" height="2.6" fill="#222"/><rect y="5.2" width="16" height="2.6" fill="#222"/><rect y="10.4" width="16" height="2.6" fill="#222"/></svg>
  </div>
  <div class="abs hero-title"><strong>CASA CERTIFIED COMPANY AND</strong><span>CASA ENDORSED PILOT</span></div>
</header>

<section class="welcome">
  <h1 class="abs section-title" style="top:78px">WELCOME TO KESTREL LIFT RENTALS</h1>
  <p class="abs section-lead" style="top:134px">CASA certified company and CASA endorsed pilot, with Full Public Liability Insurance. All operating licences are in place and are carried on<br>the operator. All drones are maintained to full CASA compliance standards</p>

  <div class="abs feature" style="left:119px;top:270px">
    <svg width="86" height="80" viewBox="0 0 86 80">
      <circle cx="30" cy="18" r="15" fill="#35467a"/><path d="M2 78c0-24 12-36 28-36s28 12 28 36z" fill="#35467a"/>
      <circle cx="62" cy="36" r="11" fill="#35467a"/><path d="M44 78c0-18 8-28 20-28s20 10 20 28z" fill="#35467a"/>
    </svg>
    <h3>Hire for parties</h3>
    <p>Lorem Ipsum is simply dummy text of the printing and typesetting industry. Lorem Ipsum has been the industry's...</p>
  </div>
  <div class="abs feature" style="left:450px;top:270px">
    <svg width="116" height="80" viewBox="0 0 116 80">
      <path d="M22 6 L112 18 L104 40 L18 26 Z" fill="#35467a"/><rect x="18" y="4" width="96" height="6" rx="3" fill="#35467a" transform="rotate(7 66 7)"/>
      <rect x="48" y="36" width="12" height="18" fill="#35467a"/><path d="M10 52 h40 v10 h-30 v16 h-10z" fill="#35467a"/>
    </svg>
    <h3>Surveillance</h3>
    <p>Lorem Ipsum is simply dummy text of the printing and typesetting industry. Lorem Ipsum has been the industry's...</p>
  </div>
  <div class="abs feature" style="left:770px;top:270px">
    <svg width="70" height="92" viewBox="0 0 70 92">
      <rect x="14" y="2" width="38" height="66" rx="5" fill="#35467a"/><rect x="19" y="10" width="28" height="48" fill="#fff"/>
      <rect x="26" y="30" width="14" height="12" rx="2" fill="#35467a"/><path d="M29 30v-5a4 4 0 0 1 8 0v5" stroke="#35467a" stroke-width="2.5" fill="none"/>
      <path d="M8 40 c-6 14 -2 34 12 48 h30 c6-8 10-18 10-30 v-14 c0-4-6-4-6 0 v8 h-6 v-10" stroke="#35467a" stroke-width="5" fill="none" stroke-linejoin="round"/>
    </svg>
    <h3>Security</h3>
    <p>Lorem Ipsum is simply dummy text of the printing and typesetting industry. Lorem Ipsum has been the industry's...</p>
  </div>
</section>

<section class="videos">
  <div class="abs monitor">
    <div class="monitor-bezel"></div>
    <div class="monitor-screen" role="img" aria-label="Video still of a drone flying over a city skyline at sunset"></div>
    <div class="monitor-chin"></div>
    <div class="monitor-stand"></div>
  </div>
  <div class="abs video-copy">
    <div class="eyebrow">SPORTING EVENTS</div>
    <h2>WATCH THE VIDEOS</h2>
    <p>Lorem Ipsum is simply dummy text of the printing and typesetting industry. Lorem Ipsum has been the industry's standard dummy text ever since the 1500s, when an unknown printer took a galley of type and scrambled it to make a type specimen book. It has survived not only five centuries, but also the leap into electronic typesetting, remaining essentially unchanged. It was popularised in the 1960s with the release of Letraset sheets containing Lorem Ipsum passages, and more recently...</p>
    <a class="btn">Click here for more info</a>
  </div>
</section>

<section class="posts">
  <h2 class="abs section-title" style="top:68px">RECENT POSTS</h2>
  <p class="abs section-lead" style="top:126px">CASA certified company and CASA endorsed pilot, with Full Public Liability Insurance. All operating licences are in place and are carried on<br>the operator. All drones are maintained to full CASA compliance standards</p>

  <article class="abs post" style="left:99px;top:226px">
    <div class="post-img" role="img" aria-label="Glowing digital padlock on a blue data background" style="background:linear-gradient(135deg,#06203a,#1d6fa8 55%,#0a2a48)"></div>
    <h4>Lorem ipsum is a dummy</h4>
    <p>CASA certified company and CASA endorsed pilot, with Full Public Liability Insurance.</p>
  </article>
  <article class="abs post" style="left:358px;top:226px">
    <div class="post-img" role="img" aria-label="Multirotor drone flying over green grass" style="background:linear-gradient(180deg,#c9dfe9,#7aa14a 55%,#3f6a22)"></div>
    <h4>Lorem ipsum is a dummy</h4>
    <p>CASA certified company and CASA endorsed pilot, with Full Public Liability Insurance.</p>
  </article>
  <article class="abs post" style="left:614px;top:226px">
    <div class="post-img" role="img" aria-label="Upward view of glass office towers against a blue sky" style="background:linear-gradient(180deg,#4f86c4,#a9c3dc 50%,#5b6470)"></div>
    <h4>Lorem ipsum is a dummy</h4>
    <p>CASA certified company and CASA endorsed pilot, with Full Public Liability Insurance.</p>
  </article>
  <article class="abs post" style="left:873px;top:226px">
    <div class="post-img" role="img" aria-label="Technician assembling a large camera drone" style="background:linear-gradient(135deg,#d9d9d9,#8a8a8a 50%,#2e2e2e)"></div>
    <h4>Lorem ipsum is a dummy</h4>
    <p>CASA certified company and CASA endorsed pilot, with Full Public Liability Insurance.</p>
  </article>
</section>

<section class="clients">
  <h2 class="abs section-title" style="top:58px">OUR CLIENTS</h2>
  <p class="abs section-lead" style="top:112px">CASA certified company and CASA endorsed pilot, with Full Public Liability Insurance. All operating licences are in place and are carried on<br>the operator. All drones are maintained to full CASA compliance standards</p>
  <div class="abs client" style="left:162px"><i></i>Brightfold</div>
  <div class="abs client" style="left:382px">Veltra</div>
  <div class="abs client" style="left:603px">Norvane</div>
  <div class="abs client" style="left:825px"><i></i>Quillo</div>
</section>

<footer class="site-footer">
  <div class="abs footer-links">Home<span class="sep">/</span>About us<span class="sep">/</span>Services<span class="sep">/</span>Videos<span class="sep">/</span>Contact Us</div>
  <div class="abs copyright">© 2015, Kestrel Lift Rentals, All Rights Reserved</div>
  <div class="abs social" aria-label="Social links"><i></i><i></i><i></i><i></i><i></i></div>
</footer>

</body>
</html>
```